Corporate-Design für kommerzielle IT-Beratung/Unternehmensberatung
Zielgruppe
kommerzielle IT-Beratung / Unternehmensberatung
Zielgruppe sind IT-Leiter, CIO, CFO von großen Mittelständischen Unternehmen
Aufgabenstellung
Berater, seriös und neutral, Experte, IT, kommerziell, analytisch, modern

```html
<!DOCTYPE html>
<html lang="de">
<head>
<meta charset="utf-8">
<title>Briefbogen – Dr. Reiber Sourcing Partner</title>
<link rel="stylesheet" href="https://fonts.googleapis.com/css2?family=Montserrat:wght@400;500;600&family=Arimo:wght@400&display=swap">
<style>
  :root{
    --bg:#cdcdcd;
    --paper:#fafafa;
    --red:#c1202a;
    --grey:#5f5f5f;
    --ink:#222;
    --muted:#555;
    --faint-red:rgba(193,32,42,0.08);
  }
  *{box-sizing:border-box;margin:0;padding:0}
  html,body{width:1200px;height:960px;overflow:hidden;background:var(--bg)}
  body{position:relative;font-family:'Montserrat',sans-serif;color:var(--ink)}
  .letterhead{
    position:absolute;left:282px;top:30px;width:636px;height:900px;
    background:linear-gradient(135deg,#fdfdfd 0%,#f4f4f4 100%);
    box-shadow:0 18px 30px rgba(0,0,0,0.18);
    overflow:hidden;
  }
  .sender-line{position:absolute;left:52px;top:150px;font-size:6.5px;color:var(--muted);letter-spacing:.2px}
  .sender-line .firm{color:var(--red)}
  .brand{position:absolute;right:44px;top:92px;display:flex;align-items:center;gap:10px}
  .brand-mark{width:14px;height:14px;border-radius:50%;background:var(--red)}
  .brand-name{font-weight:600;font-size:15px;color:var(--red);letter-spacing:.5px;line-height:1.15;text-transform:uppercase;text-align:left}
  .contact-block{
    position:absolute;right:44px;top:150px;width:186px;
    border-left:1px solid var(--red);padding-left:10px;
    font-size:8px;line-height:1.55;color:#333;letter-spacing:.2px;
  }
  .contact-block .vat{margin-top:4px;font-weight:600;color:var(--ink)}
  .watermark{
    position:absolute;left:50%;top:46%;transform:translate(-50%,-50%);
    display:flex;align-items:center;gap:18px;
  }
  .watermark-circle{width:60px;height:60px;border-radius:50%;background:var(--faint-red)}
  .watermark-name{font-weight:600;font-size:96px;color:var(--faint-red);letter-spacing:6px}
  .footer{position:absolute;left:0;right:0;bottom:0;height:120px;font-family:'Arimo',sans-serif;font-size:7.2px;line-height:1.4;color:var(--ink)}
  .footer-col{position:absolute;bottom:44px}
  .footer-col .label{margin-bottom:4px}
  .owner{left:42px}
  .contact{left:228px}
  .contact li{list-style:none;display:flex;align-items:center;gap:5px}
  .contact svg{width:7px;height:7px;flex:none}
  .bank{left:440px}
  .footer-bands{position:absolute;left:0;bottom:0;width:636px;height:22px}
</style>
</head>
<body>
  <main class="letterhead">
    <p class="sender-line"><span class="firm">Dr. Reiber Sourcing Partner,</span> Lindenweg 7, D-70199 Musterstadt</p>

    <div class="brand">
      <span class="brand-mark"></span>
      <p class="brand-name">Dr. Reiber<br>Sourcing Partner</p>
    </div>

    <address class="contact-block" style="font-style:normal">
      Lindenweg 7<br>
      D-70199 Musterstadt<br>
      info@Reiber-Sourcing-Partner.de
      <p class="vat">Ust-IDNr. DE 987654321</p>
    </address>

    <div class="watermark" aria-hidden="true">
      <span class="watermark-circle"></span>
      <span class="watermark-name">RSP</span>
    </div>

    <footer class="footer">
      <div class="footer-col owner">
        <p class="label">Inhaber:</p>
        <p>Dr. Anton Reiber<br>Lindenweg 7<br>D-70199 Musterstadt</p>
      </div>
      <div class="footer-col contact">
        <p class="label">Kontakt:</p>
        <ul>
          <li><svg viewBox="0 0 10 10"><circle cx="5" cy="5" r="4.2" fill="none" stroke="#c1202a" stroke-width="1"/><path d="M3.5 3.2l1 1-0.5 0.6 1.2 1.2 0.6-0.5 1 1-0.8 0.8C4.8 7 3.2 5.4 2.9 4z" fill="#c1202a"/></svg>+49 151 55501234</li>
          <li><svg viewBox="0 0 10 10"><rect x="1.5" y="2.5" width="7" height="5" fill="none" stroke="#c1202a" stroke-width="1"/><path d="M1.5 2.5l3.5 3 3.5-3" fill="none" stroke="#c1202a" stroke-width="1"/></svg>Anton@Reiber-Sourcing-Partner.de</li>
          <li><svg viewBox="0 0 10 10"><circle cx="5" cy="5" r="4.2" fill="none" stroke="#c1202a" stroke-width="1"/><circle cx="5" cy="5" r="2" fill="none" stroke="#c1202a" stroke-width="1"/></svg>www.reiber-sourcing-partner.de</li>
        </ul>
      </div>
      <div class="footer-col bank">
        <p class="label">Bankverbindung:</p>
        <p>MSB – Musterstädter Bank<br>IBAN : DE00 1000 0000 0000 0000 00<br>BIC: MUSTDEX1001</p>
      </div>
      <svg class="footer-bands" viewBox="0 0 636 22" preserveAspectRatio="none" aria-hidden="true">
        <path d="M0 8 H440 Q452 8 458 22 H0 Z" fill="var(--grey)"/>
        <path d="M460 22 Q464 8 476 8 H636 V22 Z" fill="var(--red)"/>
      </svg>
    </footer>
  </main>
</body>
</html>
```